Haldor Snekker AS
Buiness cards for haldor snekker as
Haldor Snekker AS - Construction
Creative Brief
Simple
Tobias Kranveldt
CEO
Lerkeskogveien 14 0587 OSLO Norway
post@haldorsnekker.example
www.haldorsnekker.example
Org. nr.: 836 402 517
Its for a company that expanse fast within big building sites
come up with something!?! we make your investment possible

```html
<!DOCTYPE html>
<html lang="no">
<head>
<meta charset="utf-8">
<title>Haldor Snekker AS – Visittkort</title>
<link rel="stylesheet" href="https://fonts.googleapis.com/css2?family=Open+Sans:wght@400;600;700&display=swap">
<style>
  :root {
    --bg: #3b3b3d;
    --card: #ffffff;
    --blue: #2d5187;
    --blue-dark: #1f3a63;
    --ink: #3a3a3a;
    --muted: #6b6b6b;
    --rule: #c9c9c9;
    --accent-line: #3c3c3c;
  }
  * { box-sizing: border-box; margin: 0; padding: 0; }
  html, body { width: 1200px; height: 852px; overflow: hidden; }
  body {
    background: var(--bg);
    font-family: "Open Sans", Arial, sans-serif;
    color: var(--ink);
    position: relative;
  }
  .card {
    position: absolute;
    width: 520px;
    height: 300px;
    background: var(--card);
    border-radius: 22px;
    overflow: hidden;
    box-shadow: 0 10px 26px rgba(0,0,0,.45);
  }
  .card--primary { left: 60px; top: 100px; }
  .card--alt { left: 620px; top: 452px; }
  .card__swoosh { position: absolute; inset: 0; width: 100%; height: 100%; }

  .brand {
    position: absolute;
    display: flex;
    align-items: center;
    gap: 10px;
  }
  .brand__mark { width: 26px; height: 26px; background: var(--blue); flex: none; }
  .brand__name {
    font-weight: 700;
    font-size: 25px;
    letter-spacing: 1px;
    color: var(--blue-dark);
    white-space: nowrap;
  }
  .card--primary .brand { left: 0; right: 0; top: 48px; justify-content: center; }
  .card--alt .brand { left: 36px; top: 140px; gap: 8px; }
  .card--alt .brand__mark { width: 22px; height: 22px; }
  .card--alt .brand__name { font-size: 18px; letter-spacing: .5px; }

  .person__name { font-weight: 600; font-size: 16px; color: var(--blue); }
  .person__role { font-size: 11px; color: var(--muted); margin-top: 4px; }
  .person__address { font-size: 11px; line-height: 1.5; color: var(--muted); margin-top: 8px; }

  .card--primary .person { position: absolute; right: 292px; top: 160px; text-align: right; }
  .card--primary .divider {
    position: absolute; left: 242px; top: 150px; width: 1px; height: 100px; background: var(--rule);
  }
  .card--primary .contact { position: absolute; left: 258px; top: 152px; }
  .card--alt .person { position: absolute; left: 288px; top: 40px; }
  .card--alt .contact { position: absolute; left: 288px; top: 138px; }
  .card--alt .contact li { height: 18px; }

  .contact { list-style: none; font-size: 11px; color: var(--muted); }
  .contact li { display: flex; align-items: center; gap: 7px; height: 19px; white-space: nowrap; }
  .contact svg { width: 11px; height: 11px; flex: none; fill: var(--ink); }
</style>
</head>
<body>

<section class="card card--primary" aria-label="Visittkort, forside">
  <svg class="card__swoosh" viewBox="0 0 520 300" aria-hidden="true">
    <path d="M0 0 H110 C50 20 12 90 0 170 Z" fill="var(--blue)"/>
    <path d="M124 0 C56 22 16 96 0 186" fill="none" stroke="var(--accent-line)" stroke-width="3"/>
    <path d="M520 300 H400 C460 285 505 220 520 110 Z" fill="var(--blue)"/>
    <path d="M386 300 C452 284 500 214 520 94" fill="none" stroke="var(--accent-line)" stroke-width="3"/>
  </svg>

  <div class="brand">
    <span class="brand__mark"></span>
    <span class="brand__name">HALDOR SNEKKER</span>
  </div>

  <div class="person">
    <p class="person__name">Tobias Kranveldt</p>
    <p class="person__role">CEO</p>
    <p class="person__address">Lerkeskogveien 14<br>0587 OSLO, Norway</p>
  </div>

  <div class="divider"></div>

  <ul class="contact">
    <li>Lin : 836 402 517</li>
    <li><svg viewBox="0 0 12 12"><rect x="3" y="0" width="6" height="12" rx="1"/></svg>+47 4100 5823</li>
    <li><svg viewBox="0 0 12 12"><rect x="3" y="0" width="6" height="3"/><rect x="0" y="3" width="12" height="6" rx="1"/><rect x="3" y="8" width="6" height="4"/></svg>+47 2200 6419</li>
    <li><svg viewBox="0 0 12 12"><path d="M0 2h12v8H0z M0 2l6 5 6-5" stroke="#fff" stroke-width="0.8"/></svg>post@haldorsnekker.example</li>
    <li><svg viewBox="0 0 12 12"><circle cx="6" cy="6" r="6"/></svg>www.haldorsnekker.example</li>
  </ul>
</section>

<section class="card card--alt" aria-label="Visittkort, bakside">
  <svg class="card__swoosh" viewBox="0 0 520 300" aria-hidden="true">
    <path d="M0 56 C18 150 66 236 150 300 H0 Z" fill="var(--blue)"/>
    <path d="M0 40 C20 144 72 236 166 300" fill="none" stroke="var(--accent-line)" stroke-width="3"/>
    <path d="M520 160 C506 232 474 280 440 300 H520 Z" fill="var(--blue)"/>
    <path d="M520 144 C504 226 468 278 424 300" fill="none" stroke="var(--accent-line)" stroke-width="3"/>
  </svg>

  <div class="brand">
    <span class="brand__mark"></span>
    <span class="brand__name">HALDOR SNEKKER</span>
  </div>

  <div class="person">
    <p class="person__name">Tobias Kranveldt</p>
    <p class="person__role">CEO</p>
  </div>

  <ul class="contact">
    <li>Lerkeskogveien 14</li>
    <li>0587 OSLO, Norway</li>
    <li>Lin : 836 402 517</li>
    <li><svg viewBox="0 0 12 12"><rect x="3" y="0" width="6" height="12" rx="1"/></svg>+47 4100 5823</li>
    <li><svg viewBox="0 0 12 12"><rect x="3" y="0" width="6" height="3"/><rect x="0" y="3" width="12" height="6" rx="1"/><rect x="3" y="8" width="6" height="4"/></svg>+47 2200 6419</li>
    <li><svg viewBox="0 0 12 12"><path d="M0 2h12v8H0z M0 2l6 5 6-5" stroke="#fff" stroke-width="0.8"/></svg>post@haldorsnekker.example</li>
    <li><svg viewBox="0 0 12 12"><circle cx="6" cy="6" r="6"/></svg>www.haldorsnekker.example</li>
  </ul>
</section>

</body>
</html>
```